Wanted: A Simple yet Awesome Blog Hero Image

We need a hero image (blog graphic header) to replace our existing one: https://www.brantwellsupply.com//blog/soil-classification-foundation-and-pavement-design-starts-here
Want something to reflect what the blog article is about and is a reflection of the title.

Note: we are not in love with any of our hero graphics

Industry/Entity Type

Construction

Colors

Designer to choose colors to be used in the design.

Requirements
Must have
• Width must be 715px
• Height must not exceed 400px
• Content on graphic should be: Soil Classification: Foundation and Pavement Design Starts Here
Nice to have
• a product shown that is mentioned in the blog
Should not have
• a product with a Carraway logo

```html
<!DOCTYPE html>
<html lang="en">
<head>
<meta charset="utf-8">
<title>Soil Classification: Foundation and Pavement Design Starts Here</title>
<link href="https://fonts.googleapis.com/css2?family=Arimo:ital,wght@0,400;0,700;1,700&family=Montserrat:wght@400;700&family=Open+Sans:wght@400&display=swap" rel="stylesheet">
<style>
:root{
  --navy:#062f5e;
  --navy-dark:#002552;
  --text:#5a5a5a;
  --link:#1b2a44;
  --orange:#f7941d;
  --header-top:#ffffff;
  --header-bottom:#d9dadc;
  --soil-1:#4a3b2f;
  --soil-2:#2a211a;
  --share-a:#3b5998;
  --share-b:#1da1f2;
  --share-c:#0077b5;
  --share-d:#7f7f7f;
  --share-e:#f26a4f;
  --row:#f2f2f2;
}
*{box-sizing:border-box;margin:0;padding:0}
html,body{width:1200px;height:800px;overflow:hidden;background:#fff}
body{font-family:"Arimo",Arial,sans-serif;position:relative}
.site-header{position:absolute;left:0;top:0;width:1200px;height:102px;background:linear-gradient(var(--header-top),var(--header-bottom))}
.corner-sieve{position:absolute;top:40px;width:70px;height:70px;border-radius:50%;background:radial-gradient(circle,#e6e6e6,#8d8d8d)}
.corner-sieve.left{left:-40px}
.corner-sieve.right{right:-40px}
.brand{position:absolute;left:108px;top:22px;display:flex;align-items:center;gap:10px}
.brand-dot{width:56px;height:56px;border-radius:50%;background:var(--navy)}
.brand-name{font-weight:700;font-size:30px;color:var(--navy);line-height:1}
.brand-name small{display:block;font-size:11px;margin-top:4px}
.tagline{position:absolute;left:452px;top:16px;width:278px;text-align:center;color:var(--navy);font-weight:700;font-style:italic;font-size:18px;line-height:20px}
.site-search{position:absolute;left:452px;top:58px;width:278px;height:28px;display:flex}
.site-search input{flex:1;border:1px solid #aaa;font:13px "Arimo",sans-serif;padding-left:6px;color:#666}
.site-search button{width:28px;border:0;background:var(--orange);display:flex;align-items:center;justify-content:center}
.quick-icons{position:absolute;left:887px;top:26px;display:flex;gap:10px}
.quick-icons span{width:40px;height:40px;border-radius:50%;background:#fff;box-shadow:0 1px 3px rgba(0,0,0,.35);display:flex;align-items:center;justify-content:center}
.main-nav{position:absolute;left:0;top:102px;width:1200px;height:35px;background:var(--navy)}
.main-nav ul{list-style:none;display:flex;position:absolute;left:102px;top:0;height:35px;border-left:1px solid #fff}
.main-nav li{color:#fff;font-weight:700;font-size:15px;height:35px;line-height:35px;text-align:center;border-right:1px solid #fff;white-space:nowrap}
.sidebar{position:absolute;left:102px;top:167px;width:245px}
.side-title{position:relative;height:45px;background:var(--navy);color:#fff;font-weight:700;font-size:16px;text-align:center;line-height:45px}
.side-title::after{content:"";position:absolute;left:50%;bottom:-8px;margin-left:-10px;border-left:10px solid transparent;border-right:10px solid transparent;border-top:8px solid var(--navy)}
.blog-search{margin-top:21px}
.blog-search input{width:245px;height:40px;border:1px solid #aaa;display:block}
.blog-search button{width:40px;height:40px;border:0;background:var(--navy);display:flex;align-items:center;justify-content:center}
.categories{margin-top:24px}
.categories ul{list-style:none;margin-top:28px}
.categories li{height:33px;font-size:15px;font-weight:700;color:var(--link);display:flex;align-items:flex-start;gap:6px;letter-spacing:.3px}
.categories li::before{content:"›";width:13px;height:13px;border:1px solid #555;font-size:11px;line-height:10px;text-align:center;margin-top:3px}
.archive{position:absolute;top:481px;width:245px}
.archive .year{margin-top:21px;height:24px;background:var(--row);font-size:13px;font-weight:700;color:#444;line-height:24px;padding-left:10px}
.archive ul{list-style:none;margin-top:14px;padding-left:30px}
.archive li{font-size:13px;font-weight:700;color:var(--link);height:33px}
.archive li::before{content:"›";margin-right:14px;color:#444}
.article{position:absolute;left:366px;top:167px;width:716px}
.article-title{height:46px;background:var(--navy);color:#fff;font-weight:700;font-size:17px;line-height:46px;padding-left:15px}
.hero{position:relative;margin-top:21px;width:715px;height:400px;background:radial-gradient(ellipse at 50% 45%,var(--soil-1),var(--soil-2));overflow:hidden;font-family:"Montserrat",sans-serif;text-align:center;color:#fff}
.hero h2{font-size:54px;font-weight:700;margin-top:20px;line-height:60px}
.hero p{font-size:27px;letter-spacing:1px}
.hero-products{position:absolute;left:10px;top:125px;width:700px;height:200px;border-radius:6px;background:linear-gradient(90deg,rgba(220,220,220,.35),rgba(170,60,60,.35) 48%,rgba(230,230,230,.4))}
.hero-cta{position:absolute;left:162px;top:330px;width:390px;height:54px;border-radius:10px;background:linear-gradient(#ffa53a,#f07a00);color:#111;font-size:29px;font-weight:700;line-height:56px}
.share{display:flex;gap:5px;margin-left:162px;height:25px}
.share span{color:#fff;font-size:9px;font-weight:700;line-height:25px;display:flex;align-items:center;justify-content:center;gap:5px}
.article-body{margin-top:18px;font-family:"Open Sans",Arial,sans-serif;font-size:16px;line-height:24px;letter-spacing:.2px;color:var(--text)}
.article-body p{margin-bottom:9px}
</style>
</head>
<body>
<header class="site-header">
  <div class="corner-sieve left" role="img" aria-label="Sieve photograph"></div>
  <div class="corner-sieve right" role="img" aria-label="Sieve photograph"></div>
  <div class="brand"><span class="brand-dot"></span><div class="brand-name">BRANTWELL<small>SUPPLY, INC.</small></div></div>
  <div class="tagline">Materials Testing Equipment<br>Contact Us Today! 800-555-0142</div>
  <form class="site-search"><input type="text" placeholder="Search for product or model #"><button type="button"><svg width="16" height="16" viewBox="0 0 16 16"><circle cx="6.5" cy="6.5" r="5" fill="none" stroke="#fff" stroke-width="2"/><line x1="10" y1="10" x2="15" y2="15" stroke="#fff" stroke-width="2"/></svg></button></form>
  <div class="quick-icons">
    <span><svg width="22" height="22" viewBox="0 0 22 22"><circle cx="8" cy="7" r="5" fill="#222"/><circle cx="8" cy="7" r="1.6" fill="#fff"/><path d="M9 11v10h3v-2h2v-2h-2v-2h2v-2h-2v-2z" fill="#222"/></svg></span>
    <span><svg width="22" height="22" viewBox="0 0 24 24"><path d="M12 2l3 7h7l-5.6 4.3 2.1 7.2L12 16.3 5.5 20.5l2.1-7.2L2 9h7z" fill="#222"/></svg></span>
    <span><svg width="22" height="22" viewBox="0 0 24 24"><path d="M2 4h3l3 11h11l3-8H7" fill="none" stroke="#222" stroke-width="2.2"/><circle cx="9" cy="19" r="2" fill="#222"/><circle cx="18" cy="19" r="2" fill="#222"/></svg></span>
    <span><svg width="24" height="22" viewBox="0 0 24 22"><rect x="1" y="2" width="15" height="11" rx="2" fill="#222"/><path d="M4 13v5l4-5z" fill="#222"/><rect x="9" y="7" width="14" height="10" rx="2" fill="#222" stroke="#fff"/><path d="M19 17v4l-4-4z" fill="#222"/><circle cx="13" cy="12" r="1" fill="#fff"/><circle cx="16" cy="12" r="1" fill="#fff"/><circle cx="19" cy="12" r="1" fill="#fff"/></svg></span>
  </div>
</header>
<nav class="main-nav"><ul>
  <li style="width:143px">PRODUCTS</li><li style="width:144px">MY BRANTWELL</li><li style="width:207px">REQUEST CATALOG</li><li style="width:105px">NEWS</li><li style="width:102px">BLOG</li><li style="width:115px">VIDEOS</li><li style="width:156px">CONTACT US</li>
</ul></nav>
<aside class="sidebar">
  <div class="side-title">BLOG SEARCH</div>
  <form class="blog-search"><input type="text" aria-label="Search blog"><button type="button"><svg width="18" height="18" viewBox="0 0 18 18"><circle cx="10" cy="8" r="5.5" fill="none" stroke="#fff" stroke-width="1.8"/><line x1="6" y1="12" x2="2" y2="16" stroke="#fff" stroke-width="1.8"/></svg></button></form>
  <div class="categories">
    <div class="side-title">BLOG CATEGORIES</div>
    <ul><li>Sieving &amp; Screening</li><li>Sampling &amp; Dividing</li><li>Aggregates</li><li>Asphalt</li><li>Concrete</li><li>Soils</li><li>General Lab</li></ul>
  </div>
  <div class="archive">
    <div class="side-title">BLOG ARCHIVE</div>
    <div class="year">2019</div>
    <ul><li>February (2)</li><li>March (1)</li></ul>
  </div>
</aside>
<main class="article">
  <h1 class="article-title">Soil Classification: Foundation and Pavement Design Starts Here</h1>
  <div class="hero">
    <div class="hero-products" role="img" aria-label="Soil color chart book, shear vane tools, test sieves and pocket penetrometer on soil"></div>
    <h2>SOIL CLASSIFICATION</h2>
    <p>FOUNDATION AND PAVEMENT</p>
    <div class="hero-cta">DESIGN STARTS HERE</div>
  </div>
  <div class="share">
    <span style="width:83px;background:var(--share-a)">Friendly</span>
    <span style="width:74px;background:var(--share-b)">Chirper</span>
    <span style="width:80px;background:var(--share-c)">WorkLink</span>
    <span style="width:68px;background:var(--share-d)">✉ Email</span>
    <span style="width:65px;background:var(--share-e)">+ More</span>
  </div>
  <div class="article-body">
    <p>Who hasn’t seen a young child eagerly digging in the ground, collecting rocks of all shapes and sizes to stuff in a pocket – and otherwise visually examining each grain of sand, clump of soil or piece of rock as if it was a precious gem?</p>
    <p>Fast forward 20-some years to the same person, still visually examining every grain of sand, clump of soil or piece of rock, but now as a civil or geotechnical engineer with a</p>
  </div>
</main>
</body>
</html>
```